Cobalt Ridge Physician Advising

I need a one-page advertisement that I can email to potential clients.

The target audience is hospital administrators.

I want it to include the logo, as attached. We specialize in Payer Denial Management. We are certified physician advisors with over 80 years combined clinical medicine experience. We have expertise in Utilization Management, Clinical Documentation Integrity, Peer to Peer Appeals and Letter Appeal Management. We win over 60% of our Peer to Peer Appeals with Managed Care Plans plans and over 50% of our first level letters.

We make sure hospitals get paid for the care they provide, I really want to emphasize that we are very effective at overturning insurance payment denials. We also provider other physician advising services. We keep our company small so that our rates are very affordable. Include that references are available.

We need to include: Contact us today, we can improve your revenue. Please 518-627-4083
or email (I will provide this later).

I want it to look professional but not bland, with maybe AI created images of a small group of physicians (mature, white coats, stethoscopes) looking at a spreadsheet on a laptop. a picture of a stack of money setting on a table, with a hand removing part of the money from the stack.

Companies like ours include Travenko, Q7, Halverick, Med-Lumora, and VantecoMD. Their websites may provide ideas.

Target Market(s)

Healthcare administrators who need to improve their hospital revenue

Industry/Entity Type

Healthcare consulting

Font styles to use
Sans Serif

Colors
0094D4
00A9DD
6FCCEA
C7EBF8
E9F6FB
00AB8E
00BBA5
67D7C9
C6EFE9
E9F9F6
FFC000
F8CF3A
FAE287
FDF2CF
FEFAEE
EE7325
F08F49
F5BC92
FAE3D3
FDF4ED
E54698
E96AAD
F1A4CE
F9D9EA
FCEFF6
6B429C
8869AF
B7A5CE
E3DAEB
F3F0F8

Requirements
Must have
• Must include that we are very successful here to appear in Peer to Peer appeals and Letter appeals
Nice to have
• Very easy to read, big bold fonts
Should not have
• I’m very afraid of having a lot of dark blues, combined with dark gold, because it may look like the colors of a health system in my area

```html
<!DOCTYPE html>
<html lang="en">
<head>
<meta charset="utf-8">
<title>Cobalt Ridge Physician Advising – Get Paid For The Care You Provide</title>
<link href="https://fonts.googleapis.com/css2?family=Poppins:wght@400;500;600;700;800&display=swap" rel="stylesheet">
<style>
  :root{
    --stage:#dde7ef;
    --blue:#0094d4;
    --blue-bright:#1f9ad8;
    --sky-top:#4f86b8;
    --sky-mid:#8fb3cf;
    --teal:#00ab8e;
    --teal-band:#12b08f;
    --gold:#ffc000;
    --highlight:#fae287;
    --orange:#ee7325;
    --ink:#1d2230;
    --white:#ffffff;
  }
  *{margin:0;padding:0;box-sizing:border-box}
  html,body{width:1200px;height:683px;overflow:hidden;background:var(--stage);font-family:"Poppins",sans-serif}
  .flyer{position:absolute;left:370px;top:16px;width:460px;height:650px;background:var(--white);overflow:hidden;box-shadow:0 10px 18px rgba(0,0,0,.18)}
  .abs{position:absolute}
  .hero-photo{left:0;top:0;width:460px;height:340px;background:linear-gradient(100deg,var(--sky-top) 0%,var(--sky-mid) 45%,#dfe8ef 70%,#c4d3df 100%)}
  .money-photo{left:262px;top:340px;width:198px;height:270px;background:radial-gradient(ellipse at 55% 42%,#c3c9b2 0%,#ddd7c7 30%,#efebe3 55%,rgba(255,255,255,0) 75%)}
  .hero-panel{left:0;top:0}
  .brand{left:0;top:18px;width:205px;text-align:center;color:var(--white);font-weight:600}
  .brand-dot{display:block;width:30px;height:30px;border-radius:50%;background:var(--white);opacity:.9;margin:0 auto 10px}
  .brand-name{font-size:17px;line-height:18px;letter-spacing:.2px}
  .brand-name small{display:block;font-size:9.5px;line-height:13px;font-weight:600;letter-spacing:.4px}
  .headline{left:14px;top:166px;color:var(--white);font-weight:800;line-height:1}
  .headline .big{display:block;color:var(--gold);font-size:40px;letter-spacing:1px}
  .headline .mid{display:block;font-size:26px;letter-spacing:1px;margin-top:1px}
  .rule{left:14px;top:268px;width:200px;height:4px;background:var(--gold)}
  .tagline{left:15px;top:279px;color:var(--white);font-size:16px;font-weight:500;line-height:20px;letter-spacing:.3px}
  .section-title{display:flex;align-items:center;gap:8px;font-weight:800;font-size:16.5px;letter-spacing:.2px}
  .stats-title{left:14px;top:367px;color:var(--teal)}
  .services-title{left:14px;top:434px;color:var(--blue)}
  .strength-title{left:14px;top:560px;color:var(--orange)}
  .list{list-style:none;font-size:8.8px;color:var(--ink);font-weight:500}
  .list li{display:flex;align-items:center;gap:6px;height:14.7px}
  .list svg{flex:none}
  .stats-list{left:14px;top:392px}
  .stats-list li span{background:var(--highlight);padding:0 2px}
  .services-list{left:14px;top:458px}
  .strength-list{left:14px;top:587px}
  .contact-band{left:0;top:0}
  .contact{right:13px;top:566px;text-align:right;color:var(--white)}
  .contact-title{font-size:17.5px;font-weight:700;letter-spacing:.8px;padding-bottom:2px;border-bottom:2px solid var(--white);display:inline-block}
  .contact-sub{font-size:9px;letter-spacing:.6px;margin-top:5px}
  .contact-line{font-size:10px;font-weight:600;display:flex;align-items:center;justify-content:flex-end;gap:4px;margin-top:1px}
</style>
</head>
<body>
<main class="flyer">
  <div class="abs hero-photo" role="img" aria-label="Two mature physicians in white coats with stethoscopes reviewing a spreadsheet on a laptop"></div>

  <svg class="abs hero-panel" width="460" height="340" viewBox="0 0 460 340">
    <polygon points="0,154 232,154 300,340 0,340" fill="var(--blue-bright)"/>
  </svg>

  <div class="abs brand">
    <span class="brand-dot"></span>
    <div class="brand-name">COBALT RIDGE<small>PHYSICIAN ADVISING</small></div>
  </div>

  <h1 class="abs headline">
    <span class="big">GET PAID</span>
    <span class="mid">FOR THE CARE</span>
    <span class="mid">YOU PROVIDE</span>
  </h1>
  <div class="abs rule"></div>
  <p class="abs tagline">Certified Physician Advisors<br>80+ Years Clinical Experience</p>

  <div class="abs money-photo" role="img" aria-label="Hand pulling banknotes from a stack of money in a jar on a wooden stand"></div>

  <h2 class="abs section-title stats-title">
    <svg width="16" height="16" viewBox="0 0 16 16"><rect x="1" y="9" width="3" height="7" fill="var(--teal)"/><rect x="6" y="6" width="3" height="10" fill="var(--teal)"/><rect x="11" y="3" width="3" height="13" fill="var(--teal)"/><path d="M1 7 L7 3 L10 5 L15 0" stroke="var(--teal)" stroke-width="1.4" fill="none"/></svg>
    SUCCESS STATS
  </h2>
  <ul class="abs list stats-list">
    <li><svg width="8" height="8" viewBox="0 0 8 8"><rect x=".5" y=".5" width="7" height="7" fill="none" stroke="var(--teal)"/><path d="M2 4 L3.5 5.5 L6.5 2" stroke="var(--teal)" fill="none"/></svg><span>Over 60% Peer to Peer Appeals win rate (Managed Care Plans)</span></li>
    <li><svg width="8" height="8" viewBox="0 0 8 8"><rect x=".5" y=".5" width="7" height="7" fill="none" stroke="var(--teal)"/><path d="M2 4 L3.5 5.5 L6.5 2" stroke="var(--teal)" fill="none"/></svg><span>Over 50% success in first-level Letter Appeals</span></li>
  </ul>

  <h2 class="abs section-title services-title">
    <svg width="16" height="16" viewBox="0 0 16 16"><rect x="5" y="1" width="9" height="10" rx="1" fill="none" stroke="var(--blue)" stroke-width="1.4"/><path d="M7 4h5M7 6.5h5" stroke="var(--blue)"/><path d="M1 14 L5 11 L10 12 L14 10" stroke="var(--blue)" stroke-width="1.8" fill="none"/></svg>
    SERVICES OFFERED
  </h2>
  <ul class="abs list services-list">
    <li><svg width="8" height="8" viewBox="0 0 8 8"><rect x=".5" y=".5" width="7" height="7" fill="none" stroke="var(--blue)"/><path d="M2 4 L3.5 5.5 L6.5 2" stroke="var(--blue)" fill="none"/></svg>Payer Denial Management</li>
    <li><svg width="8" height="8" viewBox="0 0 8 8"><rect x=".5" y=".5" width="7" height="7" fill="none" stroke="var(--blue)"/><path d="M2 4 L3.5 5.5 L6.5 2" stroke="var(--blue)" fill="none"/></svg>Utilization Management</li>
    <li><svg width="8" height="8" viewBox="0 0 8 8"><rect x=".5" y=".5" width="7" height="7" fill="none" stroke="var(--blue)"/><path d="M2 4 L3.5 5.5 L6.5 2" stroke="var(--blue)" fill="none"/></svg>Clinical Documentation Integrity</li>
    <li><svg width="8" height="8" viewBox="0 0 8 8"><rect x=".5" y=".5" width="7" height="7" fill="none" stroke="var(--blue)"/><path d="M2 4 L3.5 5.5 L6.5 2" stroke="var(--blue)" fill="none"/></svg>Peer to Peer Appeals</li>
    <li><svg width="8" height="8" viewBox="0 0 8 8"><rect x=".5" y=".5" width="7" height="7" fill="none" stroke="var(--blue)"/><path d="M2 4 L3.5 5.5 L6.5 2" stroke="var(--blue)" fill="none"/></svg>Letter Appeal Management</li>
    <li><svg width="8" height="8" viewBox="0 0 8 8"><rect x=".5" y=".5" width="7" height="7" fill="none" stroke="var(--blue)"/><path d="M2 4 L3.5 5.5 L6.5 2" stroke="var(--blue)" fill="none"/></svg>Other Physician Advising Services</li>
  </ul>

  <svg class="abs contact-band" width="460" height="650" viewBox="0 0 460 650">
    <polygon points="250,564 460,564 460,650 208,650" fill="var(--teal-band)"/>
  </svg>

  <h2 class="abs section-title strength-title">
    <svg width="16" height="16" viewBox="0 0 16 16"><rect x="6" y="1" width="6" height="15" fill="none" stroke="var(--orange)" stroke-width="1.4"/><rect x="12" y="6" width="3" height="10" fill="var(--orange)"/><rect x="1" y="8" width="4" height="8" fill="var(--orange)"/><path d="M8 4h2M8 7h2M8 10h2" stroke="var(--orange)"/></svg>
    COMPANY STRENGTH
  </h2>
  <ul class="abs list strength-list">
    <li><svg width="8" height="8" viewBox="0 0 8 8"><rect x=".5" y=".5" width="7" height="7" fill="none" stroke="var(--orange)"/><path d="M2 4 L3.5 5.5 L6.5 2" stroke="var(--orange)" fill="none"/></svg>Certified Physician Advisors</li>
    <li><svg width="8" height="8" viewBox="0 0 8 8"><rect x=".5" y=".5" width="7" height="7" fill="none" stroke="var(--orange)"/><path d="M2 4 L3.5 5.5 L6.5 2" stroke="var(--orange)" fill="none"/></svg>80+ Years Combined Clinical Experience</li>
    <li><svg width="8" height="8" viewBox="0 0 8 8"><rect x=".5" y=".5" width="7" height="7" fill="none" stroke="var(--orange)"/><path d="M2 4 L3.5 5.5 L6.5 2" stroke="var(--orange)" fill="none"/></svg>Small Company = Affordable Rate</li>
  </ul>

  <div class="abs contact">
    <div class="contact-title">CONTACT US TODAY</div>
    <div class="contact-sub">We Can Improve Your Revenue.</div>
    <div class="contact-line"><svg width="8" height="8" viewBox="0 0 8 8"><rect width="8" height="8" rx="2" fill="var(--white)"/><path d="M2.3 2 C2.3 4.5 3.5 5.7 6 5.7" stroke="var(--teal-band)" stroke-width="1.3" fill="none"/></svg>518-627-4083</div>
    <div class="contact-line"><svg width="8" height="8" viewBox="0 0 8 8"><rect width="8" height="8" rx="2" fill="var(--white)"/><rect x="1.8" y="2.5" width="4.4" height="3" fill="none" stroke="var(--teal-band)" stroke-width=".8"/><path d="M1.8 2.5 L4 4.3 L6.2 2.5" stroke="var(--teal-band)" stroke-width=".8" fill="none"/></svg>info@cobaltridgeadvising.com</div>
  </div>
</main>
</body>
</html>
```